CopperWren Works, LLC Corporate Web Site

The goal of this web site is simple. To provide an information and corporate information site for people who click on company links from other web sites. Put simply, this web site is primarily a brochure web site for the parent business. It will contain information about the company and our products with links to those products. It will be designed as a small web site but scalable as we add more products and services to our repertoire.

Please see the PDF in the uploaded files/media for more information on colors and basic guidelines, but be creative for sure.

Target Market(s)

General

Industry/Entity Type

Technology, Software

Coding

Coded - Design and coding required

Font styles to use
Other font styles liked:
• Goliath, Roboto

Colors
FFC000
F8CF3A
FAE287
FDF2CF
FEFAEE

Requirements
Must have
• Home page template, interior template, News/Press release template
Nice to have
• Searchable
Should not have
• carousels, one-page design

```html
<!DOCTYPE html>
<html lang="en">
<head>
<meta charset="utf-8">
<title>CopperWren Works, LLC – Home Page Concepts</title>
<link href="https://fonts.googleapis.com/css2?family=Bubblegum+Sans&family=Roboto:wght@400;500;700&display=swap" rel="stylesheet">
<style>
:root{
  --board:#8087c4;
  --orange:#f7941d;
  --orange-soft:#fbb040;
  --orange-pale:#fdd9a8;
  --grey:#f3f3f3;
  --grey-line:#e4e4e4;
  --text:#7a7a7a;
  --heading:#6b6b6b;
  --white:#ffffff;
  --display:"Bubblegum Sans",cursive;
  --body:"Roboto",Arial,sans-serif;
}
*{box-sizing:border-box;margin:0;padding:0}
html,body{width:1200px;height:1064px;overflow:hidden}
body{background:var(--board);font-family:var(--body);position:relative}
.concept-title{position:absolute;top:50px;width:200px;margin-left:-100px;text-align:center;font-family:var(--display);color:var(--white);font-size:18px;letter-spacing:1px}

.page{position:absolute;top:106px;width:520px;background:var(--white);transform:scale(.587);transform-origin:0 0;overflow:hidden}
.page--one{left:102px;height:1533px}
.page--two{left:466px;height:1273px}
.page--three{left:828px;height:1000px}
.page .backdrop{position:absolute;left:0;top:0;width:520px;z-index:0}
.page > *:not(.backdrop){position:absolute;z-index:1}

.site-header{top:0;left:0;width:520px;height:40px;background:var(--white);box-shadow:0 2px 4px rgba(0,0,0,.05);z-index:2!important}
.wordmark{font-family:var(--display);color:var(--orange);font-size:11px;white-space:nowrap}
.site-header .wordmark{position:absolute;left:55px;top:12px}
.main-nav{position:absolute;left:156px;top:15px;display:flex;gap:19px;font-family:var(--display);font-size:7px;color:var(--heading);text-transform:lowercase}
.btn{display:inline-block;font-family:var(--display);font-size:7px;text-transform:lowercase;color:var(--orange);border:1px solid var(--orange);border-radius:2px;text-align:center;line-height:17px;height:19px;background:var(--white)}
.btn--talk{position:absolute;left:407px;top:10px;width:56px;color:var(--heading)}
.btn--solid{background:var(--orange);color:var(--white)}

.hero-copy{left:55px;top:103px}
.hero-copy .eyebrow{font-family:var(--display);color:var(--orange);font-size:11px}
.hero-copy h1{font-family:var(--body);font-weight:500;color:var(--heading);font-size:12.5px;line-height:16px;margin-top:5px;text-transform:uppercase}
.hero-copy .actions{margin-top:12px;display:flex;gap:5px}
.hero-copy .btn{width:58px}
.art{border-radius:10px}
.art--devices{background:linear-gradient(135deg,#fff1dc,#e9edf6 60%,#fde3bf)}
.art--people{background:linear-gradient(160deg,#e8eef8,#fff0d9 55%,#f7c27a)}
.art--saas{background:radial-gradient(circle at 50% 50%,#ffe0b3,#f4f5fa 70%)}
.art--photo1{background:linear-gradient(135deg,#c9ccd3,#7d818a)}
.art--photo2{background:linear-gradient(135deg,#e7e1d8,#8a8f98)}
.art--photo3{background:linear-gradient(135deg,#6d7fc7,#e25f84 60%,#4fc1d6)}
.art--phone{background:linear-gradient(160deg,#f4f4f4,#b9bbbe 55%,#6f7174)}

.brand-block{width:94px;height:160px;background:linear-gradient(135deg,var(--orange-soft),var(--orange))}
.about-copy{width:225px}
.section-title{font-family:var(--display);color:var(--heading);font-size:18px;line-height:22px;text-transform:uppercase}
.section-title em{font-style:normal;color:var(--orange)}
.about-copy p,.feature-copy p{font-size:5.6px;line-height:8.6px;color:var(--text);margin:8px 0 12px}
.about-copy .btn,.feature-copy .btn{width:58px}

.centered-title{left:0;width:520px;text-align:center}
.card-row{left:54px;display:flex;gap:14px}
.product-card{width:127px;height:125px;background:var(--white);border:1px solid var(--grey-line);padding:14px 11px}
.product-card header{display:flex;align-items:center;gap:6px;font-size:7px;font-weight:500;color:var(--heading);text-transform:uppercase;line-height:9px}
.product-card svg{width:20px;height:24px;flex:none}
.product-card p{font-size:5.4px;line-height:7.6px;color:var(--text);margin:12px 0 10px}
.product-card a{font-family:var(--display);font-size:6px;color:var(--orange);text-decoration:none;text-transform:lowercase}
.btn--more{width:96px;left:212px}

.project-card{width:127px;height:166px;background:var(--white);border:1px solid var(--grey-line)}
.project-card .art{height:89px;border-radius:0}
.project-card h3{font-size:7.2px;font-weight:500;color:var(--heading);text-transform:uppercase;margin:12px 11px 5px;line-height:9px}
.project-card p{font-size:5.4px;line-height:7px;color:var(--text);margin:0 11px}

.news-item{display:flex;gap:7px;width:200px}
.news-date{width:32px;height:30px;border:1px solid var(--orange);text-align:center;font-family:var(--display);color:var(--heading);font-size:6px;line-height:8px;padding-top:6px;flex:none}
.news-date b{display:block;color:var(--orange);font-weight:400;font-size:7px}
.news-item h4{font-size:7px;font-weight:500;color:var(--heading);margin-bottom:3px}
.news-item p{font-size:5.4px;line-height:7px;color:var(--text)}

.site-footer{left:0;width:520px;text-align:center}
.site-footer .wordmark{display:block;font-size:13px}
.site-footer nav{display:flex;justify-content:center;gap:20px;margin-top:18px;font-family:var(--display);font-size:7px;color:var(--heading);text-transform:lowercase}
.site-footer small{display:block;margin-top:12px;font-size:6px;color:var(--text)}
</style>
</head>
<body>

<div class="concept-title" style="left:247px">Sample 1</div>
<div class="concept-title" style="left:600px">Sample 2</div>
<div class="concept-title" style="left:988px">Sample 3</div>

<!-- Concept one -->
<section class="page page--one">
  <svg class="backdrop" viewBox="0 0 520 1533" height="1533">
    <path d="M0,245 C120,215 260,285 520,235 L520,520 C380,560 160,560 0,505 Z" fill="#f3f3f3"/>
    <path d="M0,895 C150,835 300,850 400,872 C460,885 500,872 520,858 L520,1200 C380,1150 200,1170 0,1200 Z" fill="#f3f3f3"/>
    <path d="M0,870 C150,815 300,835 400,858 C460,872 500,860 520,840 L520,858 C490,882 450,888 400,878 C300,855 150,840 0,905 Z" fill="#f7941d"/>
    <path d="M230,1162 C350,1150 460,1175 520,1208" fill="none" stroke="#f7941d" stroke-width="7"/>
    <path d="M0,1360 C150,1335 350,1385 520,1350 L520,1533 L0,1533 Z" fill="#f3f3f3"/>
    <path d="M0,1380 C160,1360 340,1400 520,1372 L520,1385 C340,1410 160,1375 0,1395 Z" fill="#ebebeb"/>
  </svg>
  <header class="site-header">
    <span class="wordmark">CopperWren Works</span>
    <nav class="main-nav"><span>About</span><span>Products</span><span>Projects</span><span>Contributions</span><span>News</span></nav>
    <span class="btn btn--talk">Let's talk</span>
  </header>
  <div class="hero-copy">
    <div class="eyebrow">CopperWren Works is a</div>
    <h1>Software &amp; Applications<br>Development Organization</h1>
    <div class="actions"><span class="btn">Get started</span><span class="btn">Read more</span></div>
  </div>
  <div class="art art--devices" style="left:255px;top:85px;width:220px;height:145px" role="img" aria-label="Illustration of cloud, desktop, laptop and phone screens linked together"></div>
  <div class="brand-block" style="left:98px;top:350px" role="img" aria-label="CopperWren Works brand panel"></div>
  <div class="about-copy" style="left:225px;top:363px">
    <h2 class="section-title">About <em>CopperWren</em><br>Works, LLC</h2>
    <p>Sed ut perspiciatis unde omnis iste natus error sit voluptatem accusantium doloremque laudantium, totam rem aperiam, eaque ipsa quae ab illo inventore veritatis et quasi architecto beatae vitae dicta sunt explicabo. Nemo enim ipsam voluptatem quia voluptas sit aspernatur aut odit aut fugit, sed quia consequuntur magni dolores eos qui ratione volup tatem sequi nesciunt. Neque porro quisquam est, qui dolorem</p>
    <span class="btn">Read more</span>
  </div>
  <h2 class="section-title centered-title" style="top:600px">Our <em>Products</em> and Services</h2>
  <div class="card-row" style="top:640px">
    <article class="product-card"><header><svg viewBox="0 0 20 24"><rect x="3" y="1" width="14" height="22" rx="2" fill="none" stroke="#555" stroke-width="1.4"/><circle cx="10" cy="20" r="1" fill="#555"/></svg>Tablet-App<br>Development</header><p>Lorem ipsum dolor sit amet, cons te tur adipiscing elit, sed do eius lood tempor incididunt ut labore et olore magna aliqualouuis ipsum.</p><a>Read more</a></article>
    <article class="product-card"><header><svg viewBox="0 0 20 24"><rect x="5" y="2" width="11" height="20" rx="2" fill="none" stroke="#555" stroke-width="1.4"/><line x1="8" y1="5" x2="13" y2="5" stroke="#555"/></svg>Mobile App<br>Development</header><p>Lorem ipsum dolor sit amet, cons te tur adipiscing elit, sed do eius lood tempor incididunt ut labore et olore magna aliqualouuis ipsum.</p><a>Read more</a></article>
    <article class="product-card"><header><svg viewBox="0 0 20 24"><rect x="1" y="4" width="18" height="12" rx="1" fill="none" stroke="#555" stroke-width="1.4"/><line x1="6" y1="20" x2="14" y2="20" stroke="#555" stroke-width="1.4"/></svg>Desktop-App<br>Development</header><p>Lorem ipsum dolor sit amet, cons te tur adipiscing elit, sed do eius lood tempor incididunt ut labore et olore magna aliqualouuis ipsum.</p><a>Read more</a></article>
  </div>
  <span class="btn btn--solid btn--more" style="top:784px">View more products</span>
  <h2 class="section-title centered-title" style="top:916px">Our <em>Projects</em></h2>
  <div class="card-row" style="top:956px">
    <article class="project-card"><div class="art art--photo1" role="img" aria-label="Photo of hands working on a laptop with floating screens"></div><h3>Lorem ipsum dolor sit amet consect</h3><p>Lorem ipsum dolor sit amet, cons te lotur adipiscing elit, sed do loreius lood tempor incididun</p></article>
    <article class="project-card"><div class="art art--photo2" role="img" aria-label="Photo of two colleagues reviewing a document"></div><h3>Lorem ipsum dolor sit amet consect</h3><p>Lorem ipsum dolor sit amet, cons te lotur adipiscing elit, sed do loreius lood tempor incididun</p></article>
    <article class="project-card"><div class="art art--photo3" role="img" aria-label="Photo of a glowing digital technology interface"></div><h3>Lorem ipsum dolor sit amet consect</h3><p>Lorem ipsum dolor sit amet, cons te lotur adipiscing elit, sed do loreius lood tempor incididun</p></article>
  </div>
  <h2 class="section-title centered-title" style="top:1228px">Our <em>News</em></h2>
  <div class="news-item" style="left:55px;top:1275px"><div class="news-date">Aug 15<b>2023</b></div><div><h4>NEWS TITLE HERE</h4><p>Lorem ipsum dolor sit amet, consectetur adipiscing elit, sed do eiusmod tempor incididunt ut labore et dolore magna aliqua. Ut enim ad minim veniaquis nostrud exercitation ullamco laboris</p></div></div>
  <div class="news-item" style="left:276px;top:1275px"><div class="news-date">Aug 15<b>2023</b></div><div><h4>NEWS TITLE HERE</h4><p>Lorem ipsum dolor sit amet, consectetur adipiscing elit, sed do eiusmod tempor incididunt ut labore et dolore magna aliqua. Ut enim ad minim veniaquis nostrud exercitation ullamco laboris</p></div></div>
  <footer class="site-footer" style="top:1430px">
    <span class="wordmark">CopperWren Works</span>
    <nav><span>About</span><span>Products</span><span>Projects</span><span>Contributions</span><span>News</span></nav>
    <small>Copyright 2023 CopperWren Works, LLC</small>
  </footer>
</section>

<!-- Concept two -->
<section class="page page--two">
  <svg class="backdrop" viewBox="0 0 520 1273" height="1273">
    <path d="M0,245 C120,215 260,285 520,235 L520,520 C380,560 160,560 0,505 Z" fill="#f3f3f3"/>
    <path d="M0,1100 C150,1080 350,1125 520,1090 L520,1273 L0,1273 Z" fill="#f3f3f3"/>
    <path d="M0,1118 C160,1098 340,1140 520,1110 L520,1122 C340,1150 160,1112 0,1132 Z" fill="#ebebeb"/>
  </svg>
  <header class="site-header">
    <span class="wordmark">CopperWren Works</span>
    <nav class="main-nav"><span>About</span><span>Products</span><span>Projects</span><span>Contributions</span><span>News</span></nav>
    <span class="btn btn--talk">Let's talk</span>
  </header>
  <div class="hero-copy">
    <div class="eyebrow">CopperWren Works is a</div>
    <h1>Software &amp; Applications<br>Development Organization</h1>
    <div class="actions"><span class="btn">Get started</span><span class="btn">Read more</span></div>
  </div>
  <div class="art art--people" style="left:280px;top:58px;width:190px;height:225px" role="img" aria-label="Isometric illustration of developers around a laptop with gears and charts"></div>
  <div class="brand-block" style="left:98px;top:350px" role="img" aria-label="CopperWren Works brand panel"></div>
  <div class="about-copy" style="left:225px;top:363px">
    <h2 class="section-title">About <em>CopperWren</em><br>Works, LLC</h2>
    <p>Sed ut perspiciatis unde omnis iste natus error sit voluptatem accusantium doloremque laudantium, totam rem aperiam, eaque ipsa quae ab illo inventore veritatis et quasi architecto beatae vitae dicta sunt explicabo. Nemo enim ipsam voluptatem quia voluptas sit aspernatur aut odit aut fugit, sed quia consequuntur magni dolores eos qui ratione volup tatem sequi nesciunt. Neque porro quisquam est, qui dolorem</p>
    <span class="btn">Read more</span>
  </div>
  <h2 class="section-title centered-title" style="top:587px">Our <em>Products</em> and Services</h2>
  <div class="card-row" style="top:627px">
    <article class="product-card"><header><svg viewBox="0 0 20 24"><rect x="3" y="1" width="14" height="22" rx="2" fill="none" stroke="#555" stroke-width="1.4"/><circle cx="10" cy="20" r="1" fill="#555"/></svg>Tablet-App<br>Development</header><p>Lorem ipsum dolor sit amet, cons te tur adipiscing elit, sed do eius lood tempor incididunt ut labore et olore magna aliqualouuis ipsum.</p><a>Read more</a></article>
    <article class="product-card"><header><svg viewBox="0 0 20 24"><rect x="5" y="2" width="11" height="20" rx="2" fill="none" stroke="#555" stroke-width="1.4"/><line x1="8" y1="5" x2="13" y2="5" stroke="#555"/></svg>Mobile App<br>Development</header><p>Lorem ipsum dolor sit amet, cons te tur adipiscing elit, sed do eius lood tempor incididunt ut labore et olore magna aliqualouuis ipsum.</p><a>Read more</a></article>
    <article class="product-card"><header><svg viewBox="0 0 20 24"><rect x="1" y="4" width="18" height="12" rx="1" fill="none" stroke="#555" stroke-width="1.4"/><line x1="6" y1="20" x2="14" y2="20" stroke="#555" stroke-width="1.4"/></svg>Desktop-App<br>Development</header><p>Lorem ipsum dolor sit amet, cons te tur adipiscing elit, sed do eius lood tempor incididunt ut labore et olore magna aliqualouuis ipsum.</p><a>Read more</a></article>
  </div>
  <span class="btn btn--solid btn--more" style="top:771px">View more products</span>
  <div class="feature-copy about-copy" style="left:57px;top:885px;width:215px">
    <h2 class="section-title">Lorem <em>ipsum</em> dolor<br>sitmet nsectetur.</h2>
    <p>Sed ut perspiciatis unde omnis iste natus error sit voluptatem accusanti um doloremque laudantium, totam rem aperiam, eaque ipsa quae ab illo inventore veritatis et quasi architecto beatae vitae dicta sunt explicabo. Nemo enim ipsam voluptatem quia voluptas sit aspernatur aut odit aut sed quia consequuntur magni dolores eos qui ratione volup tatem sequi nesciunt. Neque porro quisquam est, qui dolorem</p>
    <span class="btn">Read more</span>
  </div>
  <div class="art art--phone" style="left:285px;top:842px;width:200px;height:200px" role="img" aria-label="Product photo of a silver smartphone shown front and back"></div>
  <footer class="site-footer" style="top:1170px">
    <span class="wordmark">CopperWren Works</span>
    <nav><span>About</span><span>Products</span><span>Projects</span><span>Contributions</span><span>News</span></nav>
    <small>Copyright 2023 CopperWren Works, LLC</small>
  </footer>
</section>

<!-- Concept three -->
<section class="page page--three">
  <svg class="backdrop" viewBox="0 0 520 1000" height="1000">
    <path d="M0,265 C150,290 260,355 380,355 C450,352 500,310 520,275 L520,590 C360,620 160,610 0,580 Z" fill="#f3f3f3"/>
    <path d="M0,232 C150,248 260,320 380,330 C450,335 500,290 520,245 L520,265 C490,320 440,345 380,345 C260,340 150,275 0,258 Z" fill="#fdd9a8"/>
    <path d="M0,255 C150,272 260,338 380,345 C450,348 500,308 520,262 L520,280 C490,330 440,358 380,356 C260,352 150,292 0,272 Z" fill="#fbb040"/>
    <path d="M0,830 C150,812 350,855 520,820 L520,1000 L0,1000 Z" fill="#f3f3f3"/>
    <path d="M0,848 C160,830 340,868 520,840 L520,852 C340,880 160,842 0,862 Z" fill="#ebebeb"/>
  </svg>
  <header class="site-header">
    <span class="wordmark">CopperWren Works</span>
    <nav class="main-nav"><span>About</span><span>Products</span><span>Projects</span><span>Contributions</span><span>News</span></nav>
    <span class="btn btn--talk">Let's talk</span>
  </header>
  <div class="hero-copy">
    <div class="eyebrow">CopperWren Works is :</div>
    <h1>Software &amp; Applications<br>Development Organization</h1>
    <div class="actions"><span class="btn">Get started</span><span class="btn">Read more</span></div>
  </div>
  <div class="art art--saas" style="left:258px;top:65px;width:235px;height:190px" role="img" aria-label="Line illustration of a SaaS cloud hub surrounded by service icons"></div>
  <h2 class="section-title centered-title" style="top:373px"><span>Our</span> <em>Products</em></h2>
  <div class="card-row" style="top:412px">
    <article class="product-card"><header><svg viewBox="0 0 20 24"><rect x="3" y="1" width="14" height="22" rx="2" fill="none" stroke="#555" stroke-width="1.4"/><circle cx="10" cy="20" r="1" fill="#555"/></svg>Tablet-App<br>Development</header><p>Lorem ipsum dolor sit amet, cons te tur adipiscing elit, sed do eius lood tempor incididunt ut labore et olore magna aliqualouuis ipsum.</p><a>Read more</a></article>
    <article class="product-card"><header><svg viewBox="0 0 20 24"><rect x="5" y="2" width="11" height="20" rx="2" fill="none" stroke="#555" stroke-width="1.4"/><line x1="8" y1="5" x2="13" y2="5" stroke="#555"/></svg>Mobile App<br>Development</header><p>Lorem ipsum dolor sit amet, cons te tur adipiscing elit, sed do eius lood tempor incididunt ut labore et olore magna aliqualouuis ipsum.</p><a>Read more</a></article>
    <article class="product-card"><header><svg viewBox="0 0 20 24"><rect x="1" y="4" width="18" height="12" rx="1" fill="none" stroke="#555" stroke-width="1.4"/><line x1="6" y1="20" x2="14" y2="20" stroke="#555" stroke-width="1.4"/></svg>Desktop-App<br>Development</header><p>Lorem ipsum dolor sit amet, cons te tur adipiscing elit, sed do eius lood tempor incididunt ut labore et olore magna aliqualouuis ipsum.</p><a>Read more</a></article>
  </div>
  <span class="btn btn--solid btn--more" style="top:555px">View more products</span>
  <div class="brand-block" style="left:97px;top:648px" role="img" aria-label="CopperWren Works brand panel"></div>
  <div class="about-copy" style="left:225px;top:660px">
    <h2 class="section-title">About <em>CopperWren</em><br>Works, LLC</h2>
    <p>Sed ut perspiciatis unde omnis iste natus error sit voluptatem accusantium doloremque laudantium, totam rem aperiam, eaque ipsa quae ab illo inventore veritatis et quasi architecto beatae vitae dicta sunt explicabo. Nemo enim ipsam voluptatem quia voluptas sit aspernatur aut odit aut fugit, sed quia consequuntur magni dolores eos qui ratione volup tatem sequi nesciunt. Neque porro quisquam est, qui dolorem</p>
    <span class="btn">Read more</span>
  </div>
  <footer class="site-footer" style="top:897px">
    <span class="wordmark">CopperWren Works</span>
    <nav><span>About</span><span>Products</span><span>Projects</span><span>Contributions</span><span>News</span></nav>
    <small>Copyright 2023 CopperWren Works, LLC</small>
  </footer>
</section>

</body>
</html>
```